Want to incorporate elements of all these items to make an amazing sign to welcome people to the community. The sign is 6x4 and needs to incorporate the following items:

Welcome to Corwick Meadows

Come visit the PRD sales center at 745 thistledown road
High Speed Fiber Internet
Land financing starting at $299 (No credit checks)
Let us build your dream home!
555-284-7390
We like the gold and black design no teal or blue that was another agents design. Some combination of the current sign all the stuff listed above and then design elements that tie into the truck wrap.

Target Market(s)

People visiting the neighborhood

Industry/Entity Type

real estate and construction

Font styles to use
Serif

Colors

Designer to choose colors to be used in the design.

Requirements
Must have
• PRD Home Builders Welcomes you to Corwick Meadows, Let us build your dream home, Phone number, Land financing starting at $299 NO credit checks

```html
<!DOCTYPE html>
<html lang="en">
<head>
<meta charset="UTF-8">
<title>Welcome to Corwick Meadows</title>
<link href="https://fonts.googleapis.com/css2?family=Andika:wght@400;700&family=Archivo+Black&family=Damion&display=swap" rel="stylesheet">
<style>
  :root {
    --night: #1b1c21;
    --night-soft: #262b36;
    --gold: #c9944f;
    --gold-light: #e2b476;
    --gold-mid: #d39f5a;
    --ink: #25262d;
    --white: #ffffff;
    --red: #e1001c;
    --haze-light: #f2f2f2;
    --haze-dark: #bdbdbd;
  }
  * { margin: 0; padding: 0; box-sizing: border-box; }
  html, body { width: 1200px; height: 800px; overflow: hidden; background: var(--night); }
  .sign {
    position: relative; width: 1200px; height: 800px; overflow: hidden;
    background: radial-gradient(ellipse 600px 300px at 600px 260px, var(--night-soft), var(--night) 80%);
    font-family: "Andika", sans-serif;
  }
  .welcome {
    position: absolute; top: 40px; left: 0; width: 100%;
    text-align: center; color: var(--white);
    font-family: "Andika", sans-serif; font-weight: 700; font-size: 84px; line-height: 1;
    letter-spacing: 1px;
  }
  .community-name { position: absolute; left: 56px; top: 150px; width: 1090px; height: 95px; }
  .community-name text { font-family: "Archivo Black", sans-serif; fill: var(--gold); }

  .feature-band {
    position: absolute; left: 0; top: 342px; width: 100%; height: 210px;
    background: linear-gradient(90deg, var(--gold-mid), var(--gold-light));
  }
  .band-rule { position: absolute; left: 0; top: 551px; width: 100%; height: 8px; background: var(--night); }
  .aerial-view {
    position: absolute; left: 0; top: 559px; width: 100%; height: 241px;
    background: linear-gradient(180deg, var(--haze-light), var(--haze-dark));
  }

  .feature-icon { position: absolute; top: 292px; width: 100px; height: 100px; }
  .divider { position: absolute; top: 371px; width: 4px; height: 90px; background: var(--night); }

  .feature { position: absolute; text-align: center; color: var(--ink); line-height: 1.1; }
  .feature .small { font-size: 20px; letter-spacing: 0.5px; }
  .feature .big { font-size: 31px; font-weight: 700; letter-spacing: 1px; }
  .feature .note { font-size: 16px; }
  .visit { left: 40px; width: 390px; top: 408px; }
  .visit .big { font-size: 27px; margin-top: 6px; }
  .internet { left: 483px; width: 300px; top: 412px; }
  .internet .small { font-size: 21px; margin-top: 2px; }
  .financing { left: 815px; width: 360px; top: 398px; }

  .tagline { position: absolute; left: 193px; top: 492px; width: 814px; height: 136px; }
  .tagline text { font-family: "Damion", cursive; fill: var(--white); }

  .call-today {
    position: absolute; left: 100px; top: 640px; width: 190px;
    color: var(--red); font-family: "Damion", cursive; font-size: 62px; line-height: 0.95;
    transform: rotate(-14deg); transform-origin: center;
  }
  .call-today span { display: block; }
  .call-today .second { padding-left: 0; }
  .phone { position: absolute; left: 293px; top: 660px; width: 806px; height: 100px; }
  .phone text { font-family: "Archivo Black", sans-serif; fill: var(--ink); }
</style>
</head>
<body>
<main class="sign">
  <h1 class="welcome">Welcome to</h1>
  <svg class="community-name" viewBox="0 0 1090 95" aria-label="Corwick Meadows">
    <text x="0" y="92" font-size="124" textLength="1090" lengthAdjust="spacingAndGlyphs">CORWICK MEADOWS</text>
  </svg>

  <div class="feature-band"></div>
  <div class="band-rule"></div>
  <div class="aerial-view" role="img" aria-label="Faded aerial photograph of the wooded neighborhood lots"></div>

  <svg class="feature-icon" style="left:185px" viewBox="0 0 100 100" aria-hidden="true">
    <defs>
      <linearGradient id="ring" x1="0" y1="0" x2="1" y2="1"><stop offset="0" stop-color="#2b2e37"/><stop offset="1" stop-color="#a98558"/></linearGradient>
      <linearGradient id="core" x1="0" y1="0" x2="0" y2="1"><stop offset="0" stop-color="#8a7257"/><stop offset="0.6" stop-color="#3a3a42"/><stop offset="1" stop-color="#2a2d37"/></linearGradient>
    </defs>
    <circle cx="50" cy="50" r="50" fill="url(#ring)"/>
    <circle cx="50" cy="50" r="43" fill="#fff"/>
    <circle cx="50" cy="50" r="40" fill="url(#core)"/>
    <path d="M24 46 L48 36 L48 66 L24 58 Z" fill="#fff"/>
    <ellipse cx="51" cy="51" rx="6" ry="16" fill="#fff"/>
    <circle cx="28" cy="52" r="4" fill="none" stroke="#3a3a42" stroke-width="1.5"/>
    <path d="M32 60 L38 72 L42 72 L37 60 Z" fill="#fff"/>
    <path d="M60 38 L64 32 M63 46 L70 43 M64 55 L71 56 M61 64 L67 68" stroke="#fff" stroke-width="2" stroke-linecap="round"/>
  </svg>
  <svg class="feature-icon" style="left:583px" viewBox="0 0 100 100" aria-hidden="true">
    <circle cx="50" cy="50" r="50" fill="url(#ring)"/>
    <circle cx="50" cy="50" r="43" fill="#fff"/>
    <circle cx="50" cy="50" r="40" fill="url(#core)"/>
    <path d="M27 42 A33 33 0 0 1 73 42" stroke="#fff" stroke-width="6" fill="none" stroke-linecap="round"/>
    <path d="M35 51 A22 22 0 0 1 58 45" stroke="#fff" stroke-width="6" fill="none" stroke-linecap="round"/>
    <path d="M49 67 L67 48" stroke="#fff" stroke-width="5" stroke-linecap="round"/>
    <circle cx="48" cy="68" r="4" fill="#fff"/>
  </svg>
  <svg class="feature-icon" style="left:944px" viewBox="0 0 100 100" aria-hidden="true">
    <circle cx="50" cy="50" r="50" fill="url(#ring)"/>
    <circle cx="50" cy="50" r="43" fill="#fff"/>
    <circle cx="50" cy="50" r="40" fill="url(#core)"/>
    <rect x="39" y="26" width="23" height="15" fill="#fff"/>
    <rect x="48" y="23" width="5" height="3" fill="#fff"/>
    <rect x="48" y="41" width="5" height="17" fill="#fff"/>
    <path d="M36 64 L44 56 L57 56 L65 64 Z" fill="#fff"/>
    <rect x="26" y="66" width="48" height="7" fill="#fff"/>
  </svg>

  <div class="divider" style="left:474px"></div>
  <div class="divider" style="left:788px"></div>

  <section class="feature visit">
    <p class="small">Come visit the PRD sales center at</p>
    <p class="big">745 THISTLEDOWN ROAD</p>
  </section>
  <section class="feature internet">
    <p class="big">HIGH SPEED</p>
    <p class="small">Fiber Internet</p>
  </section>
  <section class="feature financing">
    <p class="small">Land Financing</p>
    <p class="big">STARTING AT $299</p>
    <p class="note">(no credit checks)</p>
  </section>

  <svg class="tagline" viewBox="0 0 814 136" aria-label="Let us build your dream home!">
    <defs>
      <linearGradient id="pillRing" x1="0" y1="0" x2="0" y2="1"><stop offset="0" stop-color="#2c2f38"/><stop offset="1" stop-color="#a88761"/></linearGradient>
      <linearGradient id="pillFill" x1="0" y1="0" x2="0" y2="1"><stop offset="0" stop-color="#8d7659"/><stop offset="0.55" stop-color="#3b3b42"/><stop offset="1" stop-color="#2c2f39"/></linearGradient>
    </defs>
    <rect x="0" y="0" width="814" height="136" rx="68" fill="url(#pillRing)"/>
    <rect x="8" y="8" width="798" height="120" rx="60" fill="#fff"/>
    <rect x="12" y="12" width="790" height="112" rx="56" fill="url(#pillFill)"/>
    <text x="407" y="88" font-size="64" text-anchor="middle" textLength="750" lengthAdjust="spacingAndGlyphs">Let us build your dream home!</text>
  </svg>

  <p class="call-today"><span>Call</span><span class="second">today!</span></p>
  <svg class="phone" viewBox="0 0 806 100" aria-label="555-284-7390">
    <text x="0" y="96" font-size="130" textLength="806" lengthAdjust="spacingAndGlyphs">555-284-7390</text>
  </svg>
</main>
</body>
</html>
```